Etiketten-Design für Gin
Zielgruppe
Destillieren von GIN (HolgerRUM) / Zielgruppe alle die GIN Lieben :)
Aufgabenstellung
die Grunddatei besteht schon im AI Format, allerdings möchten wir gerne die Highlights in Kupfer haben wie Schrift und Holzfässer, gerne auch eigene Bilder entwerfen. Lediglich das HolgerRUM Logo (Kopf) sollte erhalten bleiben. Bitte die Datei so anlegen das die Highlights in Kupfer gedruckt (Siebdruck) werden können. Transparentes Etikett wäre super! Bei Fragen einfach melden :)

```html
<!DOCTYPE html>
<html lang="de">
<head>
<meta charset="utf-8">
<title>Holger – Barrel Aged Gin Etikett</title>
<link rel="stylesheet" href="https://fonts.googleapis.com/css2?family=Cormorant+SC:wght@500;600&display=swap">
<style>
  :root {
    --paper: #ffffff;
    --grunge: #6b6b6b;
    --grunge-light: #a9a9a9;
    --ink-grey: #5c5c5c;
    --copper: #c8643c;
    --copper-light: #e39a72;
    --copper-dark: #9c4424;
    --steel: #c9ccd3;
  }
  html, body {
    margin: 0;
    padding: 0;
    width: 1192px;
    height: 1200px;
    overflow: hidden;
    background: var(--paper);
  }
  .label {
    position: relative;
    width: 1192px;
    height: 1200px;
    background: var(--paper);
    overflow: hidden;
  }
  .grunge-frame {
    position: absolute;
    inset: 0;
    background:
      radial-gradient(ellipse 62% 58% at 50% 48%, var(--paper) 62%, rgba(255,255,255,0) 100%),
      linear-gradient(90deg, var(--grunge) 0%, var(--grunge-light) 8%, var(--paper) 20%, var(--paper) 80%, var(--grunge-light) 92%, var(--grunge) 100%),
      var(--grunge-light);
    background-blend-mode: normal, multiply, normal;
  }
  .portrait {
    position: absolute;
    left: 385px;
    top: 110px;
    width: 480px;
    height: 630px;
    border-radius: 48% 52% 44% 46% / 42% 44% 56% 58%;
    background:
      radial-gradient(circle at 60% 30%, var(--steel) 0%, rgba(201,204,211,0) 35%),
      radial-gradient(ellipse at 45% 55%, var(--copper-light) 0%, var(--copper) 55%, var(--copper-dark) 100%);
    opacity: 0.85;
  }
  .brand-name {
    position: absolute;
    left: 0;
    right: 0;
    top: 720px;
    margin: 0;
    text-align: center;
    font-family: "Cormorant SC", serif;
    font-weight: 600;
    font-size: 210px;
    line-height: 1;
    color: var(--ink-grey);
    letter-spacing: 2px;
  }
  .product-line {
    position: absolute;
    left: 0;
    right: 0;
    top: 992px;
    margin: 0;
    text-align: center;
    font-family: "Cormorant SC", serif;
    font-weight: 500;
    font-size: 62px;
    line-height: 1;
    color: var(--copper);
    letter-spacing: 1px;
  }
</style>
</head>
<body>
  <main class="label">
    <div class="grunge-frame" role="img" aria-label="Grey distressed brush texture framing the label edges"></div>
    <div class="portrait" role="img" aria-label="Sketched portrait of the distiller in copper, grey and navy strokes"></div>
    <h1 class="brand-name">Holger</h1>
    <p class="product-line">Barrel Aged Gin</p>
  </main>
</body>
</html>
```